Hey Lunagraf, this time I go to you in direct demand :)
We need a Facebook Event Cover (High definition) :
- Name of the party "VELVET TIDE"
- Date of the party "Samedi 25 novembre"
- Place of the party "Brume7" (use logo please)
- DJ's: "K-Lenz + MV"
- Style of the flyer : Vintage
- Inspiration : Old vintage Ads, old vintage objects linked to music, inspiration on google images "Vintage party" "Retro Vintage party", should be really stylish :)
- Colors : You decide, you can try, pastel colors ?

```html
<!DOCTYPE html>
<html lang="fr">
<head>
<meta charset="utf-8">
<title>Velvet Tide – Samedi 25 novembre</title>
<link rel="stylesheet" href="https://fonts.googleapis.com/css2?family=Bebas+Neue&display=swap">
<style>
  :root {
    --cream: #fbf4ea;
    --blush: #f6ece8;
    --pink: #fdc5c9;
    --peach: #fed8ae;
    --yellow: #fdf5b3;
    --mint: #c9f5d4;
    --sky: #c8e6fd;
    --ink: #161616;
    --outline: #ffffff;
  }
  html, body {
    margin: 0;
    padding: 0;
    overflow: hidden;
    background: var(--cream);
  }
  .cover {
    position: relative;
    width: 1200px;
    height: 449px;
    overflow: hidden;
    background: linear-gradient(100deg, var(--cream) 0%, #fbf6ee 45%, var(--blush) 100%);
    font-family: "Bebas Neue", "Arial Narrow", sans-serif;
  }
  .facet-art {
    position: absolute;
    left: 0;
    top: 0;
    width: 440px;
    height: 449px;
    background: linear-gradient(160deg, #f7d9cf 0%, #fbe6c9 35%, #e8e2d6 60%, #cfe6dc 100%);
    -webkit-mask-image: linear-gradient(90deg, #000 0%, rgba(0,0,0,.55) 45%, transparent 100%);
    mask-image: linear-gradient(90deg, #000 0%, rgba(0,0,0,.55) 45%, transparent 100%);
  }
  .stripe {
    position: absolute;
    display: flex;
    height: 22px;
  }
  .stripe span { width: 160px; height: 100%; }
  .stripe--top { top: 0; left: 719px; }
  .stripe--bottom { bottom: 0; left: 83px; height: 23px; }
  .c-pink { background: var(--pink); }
  .c-peach { background: var(--peach); }
  .c-yellow { background: var(--yellow); }
  .c-mint { background: var(--mint); }
  .c-sky { background: var(--sky); }

  .title {
    position: absolute;
    left: 150px;
    top: 96px;
    margin: 0;
    display: flex;
    align-items: center;
    font-weight: 400;
    font-size: 196px;
    line-height: 1;
    letter-spacing: 2px;
  }
  .title__solid {
    color: var(--pink);
    position: relative;
    z-index: 1;
  }
  .title__boxed {
    background: var(--peach);
    border-radius: 30px;
    padding: 6px 26px 0 18px;
    margin-left: -10px;
    color: transparent;
    -webkit-text-stroke: 3px var(--outline);
    line-height: 0.9;
    height: 172px;
    display: flex;
    align-items: center;
  }
  .venue {
    position: absolute;
    left: 985px;
    top: 140px;
    font-size: 64px;
    letter-spacing: 3px;
    color: var(--ink);
    display: flex;
    align-items: center;
    gap: 12px;
  }
  .venue__dot {
    width: 14px;
    height: 14px;
    border-radius: 50%;
    background: var(--ink);
  }
  .lineup {
    position: absolute;
    left: 144px;
    top: 281px;
    display: flex;
    align-items: center;
    font-size: 36px;
    letter-spacing: 0.5px;
    color: var(--ink);
    line-height: 1;
  }
  .lineup__bar {
    width: 151px;
    height: 28px;
    background: var(--sky);
    margin: 0 14px 0 10px;
  }
</style>
</head>
<body>
  <main class="cover">
    <div class="facet-art" role="img" aria-label="Pastel geometric facets fading in from the left edge"></div>

    <div class="stripe stripe--top">
      <span class="c-pink"></span><span class="c-peach"></span><span class="c-yellow"></span>
    </div>

    <h1 class="title">
      <span class="title__solid">VELVET</span>
      <span class="title__boxed">TIDE</span>
    </h1>

    <div class="venue"><span class="venue__dot"></span>BRUME7</div>

    <p class="lineup">
      <span class="lineup__date">SAMEDI 25 NOVEMBRE</span>
      <span class="lineup__bar"></span>
      <span class="lineup__djs">K-LENZ + MV</span>
    </p>

    <div class="stripe stripe--bottom">
      <span class="c-pink"></span><span class="c-peach"></span><span class="c-yellow"></span><span class="c-mint"></span><span class="c-sky"></span>
    </div>
  </main>
</body>
</html>
```